Iconic Festival requires a Joomla 3.x template

Wellmere Carnivals Society Inc is a not-for-profit organisation charged with the responsibility to deliver the iconic Wellmere Pear & Plum Festival.

This festival is held biennially in the town of Wellmere, located on the Queensland/New South Wales border in Australia. Since it’s humble beginnings back in 1954, the Pear & Plum Festival (originally known as “Return to Wellmere Days”) is one of Queensland’s Iconic Events attracting more than 52,000 visitors over the 3 days of the festival.

The Pear & Plum Festival celebrates the harvest of two of Wellmere and the Granite Belt’s major agricultural industries. The Festival culminates on the weekend with street performers, stalls, bands and a multicultural fiesta in the park celebrating our region’s diversity and the products we are now famous for; primarily wine.

The continued success of the Festival is its ability to adapt and reinvent itself year after year. Wellmere Carnivals Inc is now looking for a new website to reflect this success, the vibrancy of the event and the overall fun to be had.

The next Pear & Plum Harvest Festival will be the golden jubilee (50th anniversary).

Design Vision

Your template design should meet the following design requirements:

• Be designed for Joomla! 3.x CMS

• Vibrant ‘fun’ design reflecting the principles of the Festival - Apples, Grapes, Multiculturalism,
Food, Wine, Music, Entertainment

• Utilise the colours red, green. purple and gold (as it is the golden jubilee)

• Use a clean set of web fonts striking a balance between design and load time

• Have various module positions

• May not be branded by the designer

• Must be responsive

This website will be the online presence for the Festival, so should provide a framework to easily deliver information to visitors wishing to attend. It is essential that the design be compatible with as many browsers and devices as possible to provide a unified experience to all online visitors.

Target Audience(s)

The General Public: The Pear & Plum Harvest Festival appeals to a broad audience from young to old.

Sponsors: The Pear & Plum Harvest Festival could not be possible without the support of sponsors. The template design should feature a somewhat prominent position to display event sponsors to give them recognition for the valued donation.

Business: The Festival attracts a large number of street vendors and stall holders.

Volunteers: Volunteers provide a vital service ensuring the event is a success.

Media: Being an Iconic Event, the Pear & Plum Harvest Festival attracts a large amount of media attention.

Website Activities

The website will provide the following activities you may want to keep in mind when designing your template:

• Blogs (multiple)
• Sponsorship/Donations
• Event Calendar(s)
• Registration Forms
• Historical Collection
• Merchandise & Ticket Sales
• Social Media integration

A collection of images and the festival's logo can be found on dropbox - https://www.filecrate.example/sh/kq7tz20wbnf3x8/BBRRmh_LL2PTXoQwzkdRXYbMd?dl=0
Updates

Target Market(s)

Industry/Entity Type

Festival

Number of Pages Required

1 page

Font styles to use
Sans Serif
Decorative
Script

Requirements
Must have
• • Be designed for Joomla! 3.x CMS
• • Vibrant ‘fun’ design reflecting the principles of the Festival - Apples, Grapes, Multiculturalism,
• Food, Wine, Music, Entertainment
• • Utilise the colours red, green. purple and gold (as it is the golden jubilee)
• • Use a clean set of web fonts striking a balance between design and load time
• • Have various module positions
• • May not be branded by the designer
• • Must be responsive

```html
<!DOCTYPE html>
<html lang="en">
<head>
<meta charset="utf-8">
<title>Pear &amp; Plum Harvest Festival</title>
<link href="https://fonts.googleapis.com/css2?family=Jost:wght@400;500&family=Open+Sans:ital,wght@0,400;0,600;1,400&display=swap" rel="stylesheet">
<style>
:root{
  --paper:#ebe7da;
  --purple:#6b2a8f;
  --purple-light:#8a3bb5;
  --purple-dark:#3e1257;
  --heading:#5b2583;
  --text:#444;
  --white:#fff;
  --line:#cfcfcf;
}
*{box-sizing:border-box;margin:0;padding:0}
html,body{width:1200px;height:2287px;overflow:hidden}
body{position:relative;background:var(--white);font-family:"Open Sans",Arial,sans-serif;color:var(--text)}
.display{font-family:"Jost",Helvetica,sans-serif;font-weight:500}

.site-header{position:absolute;top:0;left:0;width:1200px;height:195px;background:var(--paper);display:flex;align-items:center;justify-content:center}
.brand{display:flex;flex-direction:column;align-items:center;gap:6px;font-family:"Jost",sans-serif;font-weight:500;color:var(--purple);text-align:center}
.brand-mark{width:44px;height:44px;border-radius:50%;background:var(--purple)}
.brand-name{font-size:22px;letter-spacing:1px;line-height:1.2}

.main-nav{position:absolute;top:195px;left:0;width:1200px;height:60px;background:linear-gradient(var(--purple-light),var(--purple));display:flex;padding-left:30px}
.main-nav a{font-family:"Jost",sans-serif;font-weight:500;color:var(--white);text-decoration:none;font-size:16px;line-height:60px;padding:0 29px;border-right:1px solid rgba(255,255,255,.2)}
.main-nav a:last-child{border-right:none}

.hero{position:absolute;top:255px;left:0;width:1200px;height:540px;background:linear-gradient(120deg,#6b5a3f 0%,#8e6b55 30%,#b23a40 55%,#4a5d6a 75%,#c04048 100%)}
.hero-caption{position:absolute;left:61px;top:154px;width:482px;height:270px;background:rgba(40,30,30,.55);padding:28px 18px}
.hero-caption .kicker{font-family:"Jost",sans-serif;font-size:34px;color:var(--white);font-weight:400;line-height:1.1}
.hero-caption h1{font-family:"Jost",sans-serif;font-size:36px;color:var(--white);font-weight:500;margin:8px 0 16px}
.hero-caption p{font-size:13px;color:var(--white);line-height:1.4}
.btn{display:inline-block;margin-top:22px;background:var(--purple);color:var(--white);font-size:14px;font-weight:600;padding:11px 14px;border-radius:3px}
.hero-dots{position:absolute;top:753px;left:0;width:1200px;display:flex;justify-content:center;gap:22px}
.hero-dots span{width:14px;height:14px;border-radius:50%;background:rgba(255,255,255,.45)}
.hero-dots span.active{background:var(--white)}
.hero-shadow{position:absolute;top:795px;left:200px;width:800px;height:28px;border-radius:50%;background:radial-gradient(ellipse at top,rgba(0,0,0,.35),rgba(0,0,0,0) 70%)}

.welcome{position:absolute;top:850px;left:64px;width:1072px;text-align:center}
.welcome h2{font-family:"Jost",sans-serif;font-weight:500;color:var(--heading);font-size:36px;letter-spacing:.5px}
.welcome p{margin-top:18px;font-size:14px;line-height:22px}

.events{position:absolute;top:1075px;left:0;width:1200px;height:577px;background:linear-gradient(#8438b3,#6a2896 55%,#3e1257)}
.events h2{position:absolute;left:59px;top:50px;font-family:"Jost",sans-serif;font-weight:500;color:var(--white);font-size:36px}
.event-card{position:absolute;top:133px;width:248px;height:383px;background:var(--white);box-shadow:0 22px 18px -10px rgba(0,0,0,.35)}
.event-photo{height:200px}
.event-card h3{font-family:"Jost",sans-serif;font-weight:500;color:var(--heading);font-size:19px;margin:27px 16px 12px}
.event-card p{font-size:14px;line-height:22px;margin:0 16px;color:#333}

.blog{position:absolute;top:1652px;left:0;width:1200px;height:387px}
.blog h2{position:absolute;left:61px;top:64px;font-family:"Jost",sans-serif;font-weight:500;color:var(--heading);font-size:36px}
.blog-arrows{position:absolute;top:70px;left:1075px;display:flex;gap:11px}
.blog-post{position:absolute;top:157px;width:518px;height:177px;border:1px solid var(--line);padding:11px 13px;display:flex;gap:22px}
.blog-photo{width:152px;height:150px;flex:none}
.blog-post h3{font-family:"Jost",sans-serif;font-weight:400;color:var(--heading);font-size:24px;margin-top:6px}
.blog-post time{display:block;font-style:italic;font-size:14px;margin:8px 0 8px 3px}
.blog-post p{font-size:13.5px;line-height:22px;margin-left:3px}

.site-footer{position:absolute;top:2039px;left:0;width:1200px;height:248px;background:linear-gradient(#8438b3,#5a1f80)}
.footer-nav{position:absolute;top:40px;left:0;width:1200px;display:flex;justify-content:center;gap:73px}
.footer-nav a{color:var(--white);text-decoration:none;font-size:15px}
.social{position:absolute;top:96px;left:0;width:1200px;display:flex;justify-content:center;gap:13px}
.social span{width:64px;height:64px;border-radius:50%;border:1px solid rgba(255,255,255,.6)}
.copyright{position:absolute;top:195px;left:0;width:1200px;text-align:center;color:var(--white);font-size:15px}
</style>
</head>
<body>
<header class="site-header">
  <div class="brand">
    <span class="brand-mark"></span>
    <span class="brand-name">Pear &amp; Plum Harvest Festival<br>WELLMERE</span>
  </div>
</header>

<nav class="main-nav">
  <a href="#">HOME</a><a href="#">WHAT'S ON</a><a href="#">YOUNG AMBASSADORS</a><a href="#">PLAN YOUR TRIP</a><a href="#">FESTIVAL FACTS</a><a href="#">SPONSORS</a>
</nav>

<section class="hero" role="img" aria-label="Street musicians with guitar and accordion at the festival among market stalls">
  <div class="hero-caption">
    <div class="kicker">GOLDEN</div>
    <h1>JUBILEE CELEBRATIONS</h1>
    <p>Neque porro quisquam est qui dolorem ipsum quia dolor sit amet, consectetur, adipisci velit...</p>
    <span class="btn">Read More</span>
  </div>
</section>
<div class="hero-dots"><span></span><span class="active"></span><span></span></div>
<div class="hero-shadow"></div>

<section class="welcome">
  <h2>WELCOME TO PEARANDPLUM</h2>
  <p>Nemo enim ipsam voluptatem quia voluptas sit aspernatur aut odit aut fugit, sed quia consequuntur magni dolores eos qui ratione voluptatem sequi nesciunt. Neque porro quisquam est, qui dolorem ipsum quia dolor sit amet, consectetur, adipisci velit, sed quia non numquam eius modi tempora incidunt ut labore et dolore magnam aliquam quaerat voluptatem. Ut enim ad minima veniam, quis nostrum exercitationem ullam corporis suscipit laboriosam.</p>
</section>

<section class="events">
  <h2>LATEST EVENTS</h2>
  <article class="event-card" style="left:59px">
    <div class="event-photo" role="img" aria-label="Festival fruit mascots in costume" style="background:linear-gradient(90deg,#c8352f,#5a3a7a)"></div>
    <h3>LOREM IPSUM DOLOR</h3>
    <p>Nemo enim ipsam voluptatem quia voluptas sit aspernatur aut odit aut fugit,</p>
  </article>
  <article class="event-card" style="left:336px">
    <div class="event-photo" role="img" aria-label="Festival ambassadors in evening dresses" style="background:linear-gradient(90deg,#c84050,#b08a5a,#5c2a6a)"></div>
    <h3>LOREM IPSUM DOLOR</h3>
    <p>Nemo enim ipsam voluptatem quia voluptas sit aspernatur aut odit aut fugit,</p>
  </article>
  <article class="event-card" style="left:613px">
    <div class="event-photo" role="img" aria-label="Child riding a camel at the festival" style="background:linear-gradient(90deg,#8a6a48,#b0403a,#5f7a45)"></div>
    <h3>LOREM IPSUM DOLOR</h3>
    <p>Nemo enim ipsam voluptatem quia voluptas sit aspernatur aut odit aut fugit,</p>
  </article>
  <article class="event-card" style="left:890px">
    <div class="event-photo" role="img" aria-label="Costumed performers in the street parade" style="background:linear-gradient(90deg,#a05a6a,#d08aa8,#5a8ac0)"></div>
    <h3>LOREM IPSUM DOLOR</h3>
    <p>Nemo enim ipsam voluptatem quia voluptas sit aspernatur aut odit aut fugit,</p>
  </article>
</section>

<section class="blog">
  <h2>LATEST BLOG</h2>
  <div class="blog-arrows">
    <svg width="28" height="28" viewBox="0 0 28 28" aria-label="Previous"><circle cx="14" cy="14" r="14" fill="#d4d4d4"/><path d="M16 8l-6 6 6 6M10 14h9" stroke="#fff" stroke-width="2.5" fill="none"/></svg>
    <svg width="28" height="28" viewBox="0 0 28 28" aria-label="Next"><circle cx="14" cy="14" r="14" fill="#d4d4d4"/><path d="M12 8l6 6-6 6M18 14H9" stroke="#fff" stroke-width="2.5" fill="none"/></svg>
  </div>
  <article class="blog-post" style="left:59px">
    <div class="blog-photo" role="img" aria-label="Crowd at a long outdoor festival dining table" style="background:linear-gradient(#7a8a90,#8a5a48)"></div>
    <div>
      <h3>Lorem ipsum dolor sit amet</h3>
      <time>March 07,2015</time>
      <p>Neque porro quisquam est, qui dolorem ipsum quia dolor sit amet, consectetur, adipisci velit, sed quia non numquam...</p>
    </div>
  </article>
  <article class="blog-post" style="left:624px">
    <div class="blog-photo" role="img" aria-label="Giant fruit float in the festival parade" style="background:linear-gradient(#6a6a5a,#c03030,#7a6a60)"></div>
    <div>
      <h3>Lorem ipsum dolor sit amet</h3>
      <time>March 07,2015</time>
      <p>Neque porro quisquam est, qui dolorem ipsum quia dolor sit amet, consectetur, adipisci velit, sed quia non numquam...</p>
    </div>
  </article>
</section>

<footer class="site-footer">
  <nav class="footer-nav">
    <a href="#">HOME</a><a href="#">WHAT'S ON</a><a href="#">YOUNG AMBASSADORS</a><a href="#">PLAN YOUR TRIP</a><a href="#">FESTIVAL FACTS</a><a href="#">SPONSORS</a>
  </nav>
  <div class="social" aria-label="Social media links">
    <span></span><span></span><span></span><span></span><span></span>
  </div>
  <p class="copyright">© 2015 pearandplum.example. All rights reserved.</p>
</footer>
</body>
</html>
```